Copperfield Hide Renewal Product Label

We need a design for a label to be used on bottles of leather cleaner and conditioner products that will be used in curated kits. We would like it to incorporate our business logo as well as have an area that we can fill in later with the appropriate product name as needed. We would like to see designs that use shades of brown, but we are open to other colors often seen in leather. I am including the Copperfield Hide business Logo below, however again we would prefer to have the label in various shades of browns, rather than the red and grey, more like the mock-up that I am also attaching.

*** I am attaching examples of the types of bottles that will be used. They vary in size from 8 oz to 16 oz. if you are designing a label for a spray bottle they are from 16-32 oz. ***

```html
<!DOCTYPE html>
<html lang="en">
<head>
<meta charset="utf-8">
<title>Copperfield Hide Renewal – Leather Cleaner &amp; Conditioner Labels</title>
<link rel="stylesheet" href="https://fonts.googleapis.com/css2?family=Montserrat:wght@700;800&family=Poppins:wght@500;600;700&display=swap">
<style>
  :root {
    --stage: #3a3a3c;
    --paper: #ffffff;
    --paper-shade: #ebe6e1;
    --band-dark: #3a2a22;
    --hide: #6b3a22;
    --hide-deep: #2c170e;
    --hide-bright: #8e4d28;
    --brand-ink: #5e2e18;
    --ink: #1c1c1c;
    --gold-dark: #9c7a35;
    --gold-light: #f4e6ad;
  }
  html, body {
    margin: 0;
    padding: 0;
    width: 950px;
    height: 1200px;
    overflow: hidden;
    background: var(--stage);
  }
  .label-sheet {
    display: block;
    width: 950px;
    height: 1200px;
  }
  .brand-name {
    font-family: "Poppins", sans-serif;
    font-weight: 600;
    fill: var(--brand-ink);
  }
  .product-word {
    font-family: "Poppins", sans-serif;
    font-weight: 700;
    letter-spacing: -2px;
  }
  .product-type {
    font-family: "Montserrat", sans-serif;
    font-weight: 800;
    fill: var(--paper);
  }
  .net-volume {
    font-family: "Montserrat", sans-serif;
    font-weight: 700;
    font-size: 36px;
  }
  .net-volume--dark { fill: var(--ink); }
  .net-volume--light { fill: var(--paper); }
</style>
</head>
<body>
<svg class="label-sheet" viewBox="0 0 1500 1894" xmlns="http://www.w3.org/2000/svg">
  <defs>
    <linearGradient id="gold-foil" x1="0" y1="0" x2="0" y2="1">
      <stop offset="0" stop-color="var(--gold-light)"/>
      <stop offset="0.5" stop-color="#d2b46a"/>
      <stop offset="1" stop-color="var(--gold-dark)"/>
    </linearGradient>
    <linearGradient id="hide-field" x1="0" y1="0" x2="1" y2="0">
      <stop offset="0" stop-color="var(--hide-deep)"/>
      <stop offset="1" stop-color="var(--hide-bright)"/>
    </linearGradient>
    <linearGradient id="paper-field" x1="0" y1="0" x2="1" y2="1">
      <stop offset="0" stop-color="var(--paper-shade)"/>
      <stop offset="0.45" stop-color="var(--paper)"/>
      <stop offset="1" stop-color="var(--paper-shade)"/>
    </linearGradient>
    <radialGradient id="goods-photo" cx="0.5" cy="0.5" r="0.6">
      <stop offset="0" stop-color="#b06a3a"/>
      <stop offset="0.6" stop-color="#6e3522"/>
      <stop offset="1" stop-color="#3d3733"/>
    </radialGradient>
    <linearGradient id="seat-photo" x1="0" y1="0" x2="1" y2="1">
      <stop offset="0" stop-color="#2a2624"/>
      <stop offset="1" stop-color="#0f0d0c"/>
    </linearGradient>
    <radialGradient id="item-photo" cx="0.5" cy="0.5" r="0.6">
      <stop offset="0" stop-color="#b8703e"/>
      <stop offset="1" stop-color="#ece4dc"/>
    </radialGradient>
    <clipPath id="front-label-clip"><rect x="163" y="188" width="553" height="1517"/></clipPath>
    <clipPath id="back-label-clip"><rect x="784" y="188" width="553" height="1517"/></clipPath>
  </defs>

  <!-- Label one: leather goods -->
  <g class="label label--goods" clip-path="url(#front-label-clip)">
    <rect class="label-paper" x="163" y="188" width="553" height="1517" fill="url(#paper-field)"/>
    <path class="diagonal-band" d="M163 660 Q400 560 716 356 L716 382 Q410 584 163 684 Z" fill="var(--band-dark)"/>

    <g class="brand-lockup" transform="rotate(-22 303 490)">
      <circle class="brand-dot" cx="303" cy="490" r="46" fill="var(--hide)"/>
      <text class="brand-name" x="360" y="478" font-size="36">COPPERFIELD HIDE</text>
      <text class="brand-name" x="362" y="504" font-size="18">RENEWAL, INC</text>
    </g>

    <path class="hide-field" d="M163 900 L716 1080 L716 1380 Q450 1482 163 1530 Z" fill="url(#hide-field)"/>
    <path class="lower-band" d="M163 1530 Q450 1482 716 1380 L716 1408 Q450 1510 163 1550 Z" fill="var(--band-dark)"/>

    <circle class="photo-ring" cx="452" cy="845" r="292" fill="var(--band-dark)"/>
    <circle class="photo-gap" cx="452" cy="845" r="280" fill="var(--paper)"/>
    <circle class="photo-goods" cx="452" cy="845" r="270" fill="url(#goods-photo)" role="img" aria-label="Photograph of leather bags, wallets, belts and a hat"/>

    <g class="product-title" transform="rotate(-12 440 1310)">
      <text class="product-word" x="440" y="1320" text-anchor="middle" font-size="130" fill="url(#gold-foil)">Leather</text>
      <text class="product-type" x="470" y="1372" text-anchor="middle" font-size="48">CLEANER &amp;</text>
      <text class="product-type" x="468" y="1428" text-anchor="middle" font-size="52">CONDITIONER</text>
    </g>

    <text class="net-volume net-volume--dark" x="440" y="1626" text-anchor="middle">16 oz</text>
  </g>

  <!-- Label two: car seats and everyday items -->
  <g class="label label--seats" clip-path="url(#back-label-clip)">
    <rect class="label-paper" x="784" y="188" width="553" height="1517" fill="var(--paper)"/>

    <g class="brand-lockup">
      <circle class="brand-dot" cx="1060" cy="360" r="56" fill="var(--hide)"/>
      <text class="brand-name" x="1060" y="476" text-anchor="middle" font-size="42">COPPERFIELD HIDE</text>
      <text class="brand-name" x="1060" y="506" text-anchor="middle" font-size="20">RENEWAL, INC</text>
    </g>

    <path class="hide-field" d="M784 600 Q1060 530 1337 585 L1337 1705 L784 1705 Z" fill="url(#hide-field)"/>
    <path class="arch-band" d="M784 580 Q1060 520 1337 565 L1337 590 Q1060 545 784 606 Z" fill="var(--band-dark)"/>
    <path class="accent-corner" d="M990 1705 Q1200 1620 1337 1470 L1337 1705 Z" fill="var(--hide-bright)"/>

    <path class="photo-seats" d="M784 612 Q1050 565 1300 625 Q1320 790 1150 905 Q950 1050 784 1222 Z" fill="url(#seat-photo)" role="img" aria-label="Photograph of black quilted leather car seats with red piping"/>

    <g class="item-badges">
      <circle cx="1226" cy="938" r="80" fill="var(--hide)"/>
      <circle cx="1226" cy="938" r="72" fill="url(#item-photo)" role="img" aria-label="Photograph of a tan leather armchair"/>
      <circle cx="1126" cy="1042" r="80" fill="var(--hide)"/>
      <circle cx="1126" cy="1042" r="72" fill="url(#item-photo)" role="img" aria-label="Photograph of a black leather jacket"/>
      <circle cx="1012" cy="1122" r="80" fill="var(--hide)"/>
      <circle cx="1012" cy="1122" r="72" fill="url(#item-photo)" role="img" aria-label="Photograph of a brown leather handbag"/>
      <circle cx="889" cy="1196" r="80" fill="var(--hide)"/>
      <circle cx="889" cy="1196" r="72" fill="url(#item-photo)" role="img" aria-label="Photograph of brown leather dress shoes"/>
    </g>

    <g class="product-title" transform="rotate(-12 1060 1420)">
      <text class="product-word" x="1050" y="1430" text-anchor="middle" font-size="130" fill="url(#gold-foil)">Leather</text>
      <text class="product-type" x="1090" y="1482" text-anchor="middle" font-size="48">CLEANER &amp;</text>
      <text class="product-type" x="1088" y="1538" text-anchor="middle" font-size="52">CONDITIONER</text>
    </g>

    <text class="net-volume net-volume--light" x="1190" y="1636" text-anchor="middle">16 oz</text>
  </g>
</svg>
</body>
</html>
```